A hand soap seller needs a premium label for a new product

We need a premium label for a bottle of soap. We want to write on it:
VANTROSELLA (Name)
Hypoallergenic and antibacterial hand soap
350 ml e / 11.8 fl oz (volume, http://pimaxo.ru/7K3RtWbqmeL519)
Saint Petersburg - Russia / www.vantrosella.ru
We want to see the face of a hippopotamus in the design. Use only black and white and green for accents (the color of grass). Examples of a hippopotamus are shown in the photo. Our soap is hypoallergenic. Ideal for both children and adults. Therefore, the label should appeal to adults and children.
The bottle will be white, and the soap dispenser will be black.
So I'm attaching an example of a soap design that we liked
Label size: height-78 mm, width-102 mm !!!

Target Market(s)

Mothers and children

Industry/Entity Type

Hand soap

Font styles to use
Serif

Colors

Designer to choose only greyscale colors for use in the design.

Requirements
Must have
• The face of a hippopotamus emerging from the grass, Black and white palette with elements of green (grass color)
Nice to have
• The face of a hippopotamus emerging from the grass
Should not have
• Different colors

```html
<!DOCTYPE html>
<html lang="en">
<head>
<meta charset="utf-8">
<title>Vantrosella Liquid Hand Soap Label</title>
<link rel="stylesheet" href="https://fonts.googleapis.com/css2?family=Montserrat:wght@400;500;600;800&display=swap">
<style>
  :root {
    --grass: #8cc63f;
    --grass-soft: #a3d35f;
    --ink: #1b1b1b;
    --paper: #ffffff;
  }
  * { margin: 0; padding: 0; box-sizing: border-box; }
  html, body { width: 828px; height: 1200px; overflow: hidden; background: var(--paper); }
  .label {
    position: relative;
    width: 828px;
    height: 1200px;
    background: var(--paper);
    font-family: "Montserrat", sans-serif;
    color: var(--ink);
    overflow: hidden;
  }
  .label__shapes { position: absolute; inset: 0; }
  .brand {
    position: absolute; top: 110px; left: 0; width: 100%;
    text-align: center;
    font-size: 92px; font-weight: 800; letter-spacing: 1px;
    color: var(--ink);
  }
  .claim {
    position: absolute; top: 262px; left: 0; width: 100%;
    text-align: center;
    font-size: 30px; font-weight: 500; letter-spacing: 1px;
  }
  .product {
    position: absolute; top: 320px; left: 50%; transform: translateX(-50%);
    padding: 10px 16px;
    border-top: 2px solid var(--grass);
    border-bottom: 2px solid var(--grass);
    font-size: 30px; font-weight: 600; letter-spacing: 3px;
    color: var(--grass); white-space: nowrap;
  }
  .mascot {
    position: absolute; top: 420px; left: 364px;
    width: 100px; height: 100px; border-radius: 50%;
    background: radial-gradient(circle, #e6f3d4 0%, var(--paper) 75%);
    border: 3px solid var(--grass);
  }
  .mascot-faint {
    position: absolute; left: 30px; top: 780px;
    width: 190px; height: 170px; border-radius: 40%;
    background: radial-gradient(circle, var(--grass-soft) 0%, var(--grass) 75%);
  }
  .shield { position: absolute; top: 545px; left: 369px; width: 90px; height: 104px; }
  .gentle {
    position: absolute; top: 560px; left: 470px;
    transform: rotate(-45deg); transform-origin: left top;
    font-size: 22px; font-weight: 500; color: var(--ink); white-space: nowrap;
  }
  .protection {
    position: absolute; top: 880px; left: 440px; width: 380px;
    text-align: center; color: var(--grass);
    font-size: 28px; font-weight: 500; line-height: 1.25; white-space: nowrap;
  }
  .estimated {
    position: absolute; top: 968px; left: 616px;
    width: 28px; height: 28px; border-radius: 50%;
    background: var(--grass); color: var(--ink);
    font-size: 18px; font-weight: 800; text-align: center; line-height: 28px;
  }
  .volume {
    position: absolute; top: 1030px; left: 430px; width: 400px;
    text-align: center; color: var(--paper);
    font-size: 24px; font-weight: 400; white-space: nowrap;
  }
  .rule {
    position: absolute; top: 1084px; left: 520px; width: 220px;
    border-top: 2px solid var(--paper);
  }
  .origin {
    position: absolute; top: 1118px; left: 250px; width: 570px;
    text-align: center; color: var(--paper);
    font-size: 20px; font-weight: 400; white-space: nowrap;
  }
</style>
</head>
<body>
  <main class="label">
    <svg class="label__shapes" width="828" height="1200" viewBox="0 0 828 1200">
      <polygon points="0,540 360,1200 0,1200" fill="var(--grass)"/>
      <polygon points="828,520 828,1200 150,1200" fill="var(--ink)"/>
    </svg>

    <div class="mascot-faint" role="img" aria-label="Faint outline of a hippo face decoration"></div>

    <h1 class="brand">VANTROSELLA</h1>
    <p class="claim">HYPOALLERGENIC AND ANTIBACTERIAL</p>
    <p class="product">LIQUID HAND SOAP</p>

    <div class="mascot" role="img" aria-label="Small green line drawing of a hippo face"></div>

    <svg class="shield" viewBox="0 0 90 104" aria-hidden="true">
      <path d="M45 4 L84 18 V52 C84 78 64 94 45 100 C26 94 6 78 6 52 V18 Z" fill="var(--paper)" stroke="var(--grass)" stroke-width="6"/>
      <rect x="38" y="28" width="14" height="48" fill="var(--grass)"/>
      <rect x="21" y="45" width="48" height="14" fill="var(--grass)"/>
    </svg>

    <p class="gentle">Gently Cleanses for 100% Sure</p>

    <p class="protection">Protection Against<br>100 Germs</p>
    <span class="estimated">e</span>
    <p class="volume">350 ml e / 11.8 fl oz</p>
    <div class="rule"></div>
    <p class="origin">Saint Petersburg - Russia / www.vantrosella.ru</p>
  </main>
</body>
</html>
```